Social Media Graphics - Copperfield Loop

Create 6-7 individual social media graphics (square size) to encourage folks to join our online course, using either of the text below (only one set of text per graphic:

The Lantern Ridge Method
How to Create a 7-Figure Business From Scratch
Sign Up Today!

Or

The Lantern Ridge Method
Fast-track Your Way to a Multi-Million Business!
Sign Up Today!

For the color scheme of the graphics, use 1 or 2 colors in the color palette attached; or use any colors that look nice with their outfits; AVOID using red, white and blue altogether because it will look like an Independence Day (4th of July) graphic and we don’t want that; make sure the graphics appeal to both men and women

Make sure each graphic contains 1 of the 2 pics attached; and make sure one of the graphics is all TEXT only.

Target Market(s)

men and women looking to make more money

Industry/Entity Type

entrepreneurship

Requirements
Must have
• see the text document attached
Nice to have
• We are open to a nice color design; the color palette colors are not required, especially we don't want red, white and blue used together
Should not have
• AVOID using red, white and blue altogether because it will look like an Independence Day (4th of July) graphic and we dont want that

```html
<!DOCTYPE html>
<html lang="en">
<head>
<meta charset="utf-8">
<title>The Lantern Ridge Method — Copperfield Loop</title>
<link rel="stylesheet" href="https://fonts.googleapis.com/css2?family=Montserrat:wght@400;700;800&display=swap">
<style>
  :root {
    --plum: #3a0f4a;
    --plum-deep: #220630;
    --blush: #fcd9d8;
    --title-pink: #fcd6d2;
    --gold: #f2c46d;
    --cream: #fde8e2;
    --button: #fbc9cf;
    --ink: #2a0a33;
    --photo-top: #3b3346;
    --photo-mid: #26202e;
    --photo-low: #4a3a55;
  }
  html, body {
    margin: 0;
    padding: 0;
    width: 1200px;
    height: 1200px;
    overflow: hidden;
  }
  .canvas {
    position: relative;
    width: 1200px;
    height: 1200px;
    overflow: hidden;
    background: radial-gradient(ellipse at 50% 30%, var(--plum) 0%, var(--plum) 50%, var(--plum-deep) 100%);
    font-family: "Montserrat", Arial, sans-serif;
  }
  .backdrop {
    position: absolute;
    inset: 0;
    width: 1200px;
    height: 1200px;
  }
  .headline {
    position: absolute;
    top: 63px;
    left: 0;
    width: 1200px;
    margin: 0;
    text-align: center;
    font-weight: 800;
    font-size: 118px;
    line-height: 130px;
    letter-spacing: 0;
    text-transform: uppercase;
    color: var(--title-pink);
  }
  .headline .line { display: block; }
  .headline .accent { color: var(--gold); }
  .subhead {
    position: absolute;
    top: 328px;
    left: 0;
    width: 1200px;
    margin: 0;
    text-align: center;
    font-weight: 400;
    font-size: 35px;
    line-height: 47px;
    color: var(--cream);
  }
  .subhead strong { font-weight: 700; }
  .cta {
    position: absolute;
    top: 455px;
    left: 381px;
    width: 438px;
    height: 94px;
    border-radius: 47px;
    background: var(--button);
    color: var(--ink);
    font-weight: 800;
    font-size: 37px;
    line-height: 94px;
    text-align: center;
  }
  .hosts-photo {
    position: absolute;
    left: 150px;
    top: 567px;
    width: 750px;
    height: 633px;
    border-radius: 200px 200px 0 0;
    background: linear-gradient(180deg, var(--photo-top) 0%, var(--photo-mid) 45%, var(--photo-low) 100%);
  }
</style>
</head>
<body>
<main class="canvas">
  <svg class="backdrop" viewBox="0 0 1200 1200" aria-hidden="true">
    <defs>
      <linearGradient id="arrowFill" x1="0" y1="1" x2="1" y2="0">
        <stop offset="0" stop-color="#a8326e"/>
        <stop offset="0.55" stop-color="#e2789a"/>
        <stop offset="1" stop-color="#f7b4c2"/>
      </linearGradient>
    </defs>
    <polygon class="blush-field" fill="#fcd9d8"
      points="0,1094 200,965 540,920 711,705 867,805 1040,640 1200,420 1200,1200 0,1200"/>
    <polyline class="growth-arrow" fill="none" stroke="url(#arrowFill)" stroke-width="66" stroke-linejoin="miter"
      points="-20,1015 200,885 540,840 711,622 867,722 1030,575"/>
    <polygon class="growth-arrow-head" fill="#f7b4c2"
      points="925,489 1144,455 1117,672"/>
  </svg>

  <h1 class="headline">
    <span class="line">The <span class="accent">Lantern</span></span>
    <span class="line">Ridge Method</span>
  </h1>

  <p class="subhead">How to Create a <strong>7-Figure Business</strong><br>From Scratch</p>

  <div class="cta">Sign Up Today!</div>

  <div class="hosts-photo" role="img" aria-label="Photo of the two course hosts standing side by side, smiling, one in a black turtleneck with arms crossed and one in a denim blazer"></div>
</main>
</body>
</html>
```